Coaching business needs flyer for business market

I need a flyer that I can send to HR-managers and business owners to inform them of my coaching services for organisations. We have three services: organisational- and teamcoaching, individual coaching and training programs.
I want the flyer to express calmness, solid and trustworthy coaching. As a person I am open and think out of the box.

In my logo I use a couple of colours (blue, green, orange and grey) that represent the diversity of humans. My company's name is Wrenhollow Alignment & Coaching and tag line is "Ignite your inner light".

I do not want the design to be too busy but also not too boring. I tried making something myself. Feel free to build on that design. Or feel free to start from scratch.

```html
<!DOCTYPE html>
<html lang="nl">
<head>
<meta charset="utf-8">
<title>Wrenhollow Alignment &amp; Coaching – flyer</title>
<link rel="stylesheet" href="https://fonts.googleapis.com/css2?family=Arimo:wght@400;700&display=swap">
<style>
  :root{
    --blue:#2f5f86;
    --blue-deep:#285478;
    --orange:#f4971f;
    --mint:#90d4b9;
    --white:#ffffff;
    --grey:#55595c;
    --page:#e6e6e6;
  }
  *{box-sizing:border-box;margin:0;padding:0}
  html,body{width:1200px;height:1200px;overflow:hidden;background:var(--page)}
  body{position:relative;font-family:"Arimo",Arial,sans-serif}
  .flyer{
    position:absolute;left:190px;top:20px;width:1125px;height:1593px;
    transform:scale(0.7282);transform-origin:0 0;
    background:var(--blue);overflow:hidden;color:var(--white);
  }
  .shapes{position:absolute;inset:0}
  .abs{position:absolute}
  .brand-box{
    left:335px;top:0;width:455px;height:240px;background:var(--white);
    border-radius:0 0 20px 20px;display:flex;flex-direction:column;
    align-items:center;justify-content:center;gap:14px;z-index:2;
  }
  .brand-mark{width:74px;height:74px;border-radius:50%;border:3px solid var(--grey)}
  .brand-name{font-size:46px;color:var(--grey);font-weight:400;letter-spacing:1px;line-height:1}
  .brand-tag{font-size:21px;color:var(--grey);font-weight:400;letter-spacing:1px;line-height:1}
  .dots{left:110px;top:82px;display:flex;flex-direction:column;gap:16px}
  .dots span{width:6px;height:6px;border-radius:50%;background:var(--white)}
  .bio{left:29px;top:280px;width:720px;font-size:18.5px;line-height:20.8px}
  .bio strong{font-weight:700}
  .portrait{
    left:800px;top:205px;width:290px;height:279px;border-radius:145px 145px 0 0;
    background:radial-gradient(circle at 50% 40%,#b7845f 0%,#8a5c40 55%,#3b3a52 100%);
  }
  .team-intro{left:29px;top:517px;width:960px;font-size:19px;font-weight:700;line-height:26px;color:var(--mint)}
  .photo{border-radius:50%}
  .photo-team{left:31px;top:597px;width:216px;height:216px;border:3px solid var(--orange);
    background:radial-gradient(circle at 50% 45%,#a08a74,#6d6258 60%,#4c4a48)}
  .team-list{left:276px;top:620px;list-style:none;font-size:18.5px}
  .team-list li{position:relative;padding-left:26px;height:45px}
  .team-list li::before{content:"";position:absolute;left:0;top:6px;width:12px;height:12px;border-radius:50%;background:var(--orange)}
  .photo-col{top:928px;width:218px;height:218px;border:4px solid var(--white)}
  .photo-1{left:74px;background:radial-gradient(circle at 50% 55%,#b27c6c,#8a7a70 55%,#5c6a78)}
  .photo-2{left:447px;background:radial-gradient(circle at 50% 50%,#d8cfc4,#a39a90 60%,#6c6660)}
  .photo-3{left:822px;background:radial-gradient(circle at 50% 60%,#c98a4a,#8c8c84 55%,#6f8a8c)}
  .col-head{top:1172px;font-size:18.5px;font-weight:700;line-height:22.5px;text-align:center}
  .col-list{list-style:none;text-align:center;font-size:18.5px}
  .col-list li::before{content:"";display:inline-block;width:10px;height:10px;border-radius:50%;background:var(--mint);margin-right:9px;vertical-align:2px}
  .list-1{left:20px;top:1250px;width:330px;line-height:17px}
  .list-1 li{margin-bottom:17px}
  .list-2{left:366px;top:1250px;width:380px;line-height:27px}
  .list-2 li{margin-bottom:11px}
  .list-3{left:755px;top:1252px;width:365px;line-height:21px}
  .list-3 li{margin-bottom:18px}
</style>
</head>
<body>
<main class="flyer">
  <svg class="shapes" viewBox="0 0 1125 1593" aria-hidden="true">
    <polygon points="0,300 300,120 335,120 335,197 0,197" fill="var(--blue-deep)"/>
    <polygon points="450,484 1125,484 1125,700 700,1100 0,1100 0,760" fill="var(--blue-deep)" opacity="0.35"/>
    <polygon points="700,1300 1125,1000 1125,1593 950,1593" fill="var(--blue-deep)" opacity="0.6"/>
    <line x1="980" y1="88" x2="1140" y2="-25" stroke="var(--mint)" stroke-width="72" stroke-linecap="round"/>
    <rect x="0" y="197" width="1125" height="287" fill="var(--orange)"/>
    <path d="M1093 484H1125V737H1096V1040Q1096 1055 1081 1055H44Q29 1055 29 1040V893Q29 878 44 878H891V737H1093Z" fill="var(--mint)"/>
    <path d="M1074 484V706H862V878" fill="none" stroke="var(--orange)" stroke-width="14"/>
    <line x1="30" y1="1620" x2="130" y2="1550" stroke="var(--mint)" stroke-width="72" stroke-linecap="round"/>
    <path d="M390 1593L530 1500Q552 1485 574 1500L730 1593Z" fill="var(--orange)"/>
  </svg>

  <div class="abs dots"><span></span><span></span><span></span></div>

  <header class="abs brand-box">
    <div class="brand-mark"></div>
    <div class="brand-name">wrenhollow</div>
    <div class="brand-tag">alignment &amp; coaching</div>
  </header>

  <p class="abs bio"><strong>ANJALI VERHOEVEN</strong> is trainer en coach. Ze heeft ruime<br>ervaring met veranderingstrajecten binnen organisaties. Mensen<br>omschrijven haar als ‘betrokken, warm, stevig en kordaat’. Het is haar passie om<br>organisaties, teams en mensen te helpen groeien. Zij helpt weerstand te overwinnen<br>en draagt bij aan groei in zelfvertrouwen. Haar trainingen en coaching zijn erop<br>gericht om snel inzichtelijk te krijgen welke stappen men moet zetten om verder te<br>komen.Ze gelooft de veranderkracht van de mensen waar ze mee werkt. Ze is er<br>om steun en richting te bieden en laat hen zelf aan het roer.</p>

  <div class="abs portrait" role="img" aria-label="Portretfoto van de coach, lachend"></div>

  <h2 class="abs team-intro">Een organisatie waar medewerkers gemotiveerd zijn,samenwerken, communiceren zonder gedoe door<br>ORGANISATIE- of TEAM coaching:</h2>

  <div class="abs photo photo-team" role="img" aria-label="Foto van een teamsessie in een zaal"></div>

  <ul class="abs team-list">
    <li>Heb je zorgen voor of na een fusie of verandering?</li>
    <li>Wil je missie, visie &amp; strategie ontwikkelen of wijzigen?</li>
    <li>Wens je de cultuur-veranderen of verder ontwikkelen?</li>
    <li>Beoog je de samenwerking bevorderen of verbeteren?</li>
  </ul>

  <div class="abs photo photo-col photo-1" role="img" aria-label="Foto van een groepsgesprek"></div>
  <div class="abs photo photo-col photo-2" role="img" aria-label="Foto van een coachingsessie in een kamer"></div>
  <div class="abs photo photo-col photo-3" role="img" aria-label="Foto van een workshop met deelnemers in een kring"></div>

  <h3 class="abs col-head" style="left:40px;width:290px">Duurzame Inzetbaarheid door<br>INDIVIDUELE Coaching:</h3>
  <h3 class="abs col-head" style="left:366px;width:380px">Ontwikkeling &amp; Borging van kennis en<br>vakmanschap door LEERGANGEN,<br>TRAININGEN &amp; WORKSHOPS op MAAT:</h3>
  <h3 class="abs col-head" style="left:776px;width:300px;top:1170px;line-height:21px">Gedegen resultaat en kwaliteit<br>door bewezen ‘best practices’</h3>

  <ul class="abs col-list list-1">
    <li>Wens je medewerkers die<br>hun talent ten volste benutten?</li>
    <li>Verlang je meer authentieke<br>leiderschap bij je collega’s?</li>
    <li>Wil je de mensen vooruit helpen<br>in hun loopbaan?</li>
    <li>Zoek je steun voor medewerkers<br>met burn-out of re-integratie?<br>Heb je hulp nodig bij<br>outplacement trajecten?</li>
  </ul>

  <ul class="abs col-list list-2">
    <li>Leiderschap</li>
    <li>Communicatie</li>
    <li>Leren kijken met ‘systemische blik’<br>voor professionals</li>
    <li>Conflicthantering</li>
  </ul>

  <ul class="abs col-list list-3">
    <li>Neuro Linguïstisch Programmeren<br>(NLP)Transactionele Analyse</li>
    <li style="line-height:27px">Systemisch Werken:<br>Organisatieopstellingen,</li>
    <li>Familieopstellingen, Identity oriented<br>Psycho Traumaopstellingen)</li>
    <li style="line-height:27px">Somatic Experience, Ademwerk<br>en Lichaamswer</li>
  </ul>
</main>
</body>
</html>
```